TAVRO Capital Group LLC a High Risk Big Rewards company for Rich Young Entrepreneurs

We would like a very modern, powerful in the eyes of our customers, modern, minimalist feel, financial gain. this business card is for young Rich entrepreneurs who want to invest money into High Risk, Big Rewards Businesses. The card Should sell the business!! let your creativity go Wild! I pick most of the designers for this project because of your BOLD Designs, I would like this card to be Bold, Modern, Minimalist, use as many effects in your graphic Artist Mind, Do not let the Financial sound of this business to make you think Conservative that's the last thing we are! if you have a lot of money and you want to play a risky market call US
Updates

Project Deadline Extended
Reason: have not received, enough designs to choose 1st and second place, sure I have received over 100 designs but it seems most designers are submitting every card they have ever made before and calling it mine, please we are looking for fresh ideas please!

Target Market(s)

Private Risky Investors

Industry/Entity Type

Financial

Contact Information for Business Card

powerful in the eyes of our customers,modern, minimalist feel

Font styles to use
Other font styles liked:
• Modern feeling fonts

Requirements
Must have
• The Company Name is TAVRO Capital Group LLC and it must be on the CARD
• My Name, title, Cell , email
• Delvin Ashcroft G.E.D.
• Managing Member
• 555.038.6195
• delvin@tavrocapitalgroup.example
Nice to have
• try a black thick plastic card with round corners with Delvin Ashcroft GED (make sure GED is smaller than name) just on one side of the card, and my phone number with out the icons and email on the other side, this card should look like a exclusive credit card or exclusive VIP card, something you would never loose

```html
<!DOCTYPE html>
<html lang="en">
<head>
<meta charset="utf-8">
<title>TAVRO Capital Group LLC — Business Card</title>
<link href="https://fonts.googleapis.com/css2?family=Barlow:wght@400;500;700&display=swap" rel="stylesheet">
<style>
  :root {
    --page: #e7e4df;
    --card: #2a2a2a;
    --card-edge: #333333;
    --ink: #0e0e0e;
    --paper: #ffffff;
    --gold: #f3c343;
    --gold-soft: rgba(243, 195, 67, 0.3);
    --text-light: #f2f2f2;
  }
  * { margin: 0; padding: 0; box-sizing: border-box; }
  html, body {
    width: 1200px; height: 1000px; overflow: hidden;
    background: var(--page);
    font-family: "Barlow", Arial, sans-serif;
  }
  .canvas { position: relative; width: 1200px; height: 1000px; }
  .card {
    position: absolute;
    width: 692px; height: 400px;
    border-radius: 18px;
    overflow: hidden;
    background: radial-gradient(ellipse at 60% 30%, var(--card-edge), var(--card) 70%);
    box-shadow: 0 6px 14px rgba(0,0,0,0.25);
  }
  .card--front { left: 260px; top: 88px; }
  .card--back  { left: 262px; top: 533px; }
  .card .bands { position: absolute; left: 0; top: 0; }
  .bulb-art {
    position: absolute;
    border-radius: 45% 45% 30% 30%;
    background: radial-gradient(ellipse at 50% 45%, var(--gold) 0 24%, var(--gold-soft) 46%, transparent 70%);
  }
  .card--front .bulb-art { left: 40px; top: 8px; width: 240px; height: 270px; }
  .card--back .bulb-art { left: 40px; top: 50px; width: 240px; height: 250px; }
  .company {
    position: absolute;
    color: var(--gold);
    font-weight: 700;
    font-size: 29px;
    line-height: 1.2;
    letter-spacing: 0.2px;
    white-space: nowrap;
    padding-bottom: 4px;
    border-bottom: 2px dashed var(--gold);
  }
  .card--front .company { left: 312px; top: 30px; }
  .card--back .company { left: 286px; top: 150px; }
  .holder-name {
    position: absolute; left: 314px; top: 142px;
    color: var(--ink); font-size: 31px; font-weight: 400; line-height: 1.2;
    white-space: nowrap; transform: rotate(-2deg); transform-origin: left center;
  }
  .holder-title {
    position: absolute; left: 318px; top: 208px;
    color: var(--text-light); font-size: 32px; font-weight: 500; line-height: 1.2;
    white-space: nowrap;
  }
  .contact {
    position: absolute; left: 210px; white-space: nowrap;
    font-size: 27px; font-weight: 400; line-height: 1;
  }
  .contact--phone { top: 292px; color: var(--text-light); }
  .contact--email { top: 344px; color: var(--ink); }
  .contact-icon { position: absolute; left: 157px; width: 24px; height: 24px; }
  .contact-icon--phone { top: 300px; }
  .contact-icon--email { top: 350px; }
</style>
</head>
<body>
<main class="canvas">

  <section class="card card--front" aria-label="Card front">
    <div class="bulb-art" role="img" aria-label="Sketched glowing light bulb illustration with radiating lines"></div>
    <svg class="bands" width="692" height="400" viewBox="0 0 692 400" aria-hidden="true">
      <polygon points="300,127 692,92 692,176 298,198" fill="var(--paper)"/>
      <polygon points="300,133 692,102 692,110 300,141" fill="var(--ink)"/>
      <rect x="190" y="256" width="502" height="70" fill="var(--ink)"/>
      <polygon points="190,324 692,310 692,380 190,380" fill="var(--paper)"/>
      <rect x="0" y="292" width="190" height="56" fill="var(--paper)"/>
      <rect x="0" y="348" width="190" height="32" fill="var(--ink)"/>
    </svg>
    <div class="company">TAVRO Capital Group LLC</div>
    <div class="holder-name">Delvin Ashcroft G.E.D.</div>
    <div class="holder-title">Managing Member</div>
    <svg class="contact-icon contact-icon--phone" viewBox="0 0 24 24" aria-hidden="true">
      <circle cx="12" cy="12" r="10" fill="none" stroke="var(--ink)" stroke-width="1.6"/>
      <path d="M9 7c-1 1-1 3 0 5s3 4 5 5c1 0 2-1 2-1l-2-2-1 1c-1-1-2-2-3-3l1-1-2-4z" fill="var(--ink)"/>
    </svg>
    <svg class="contact-icon contact-icon--email" viewBox="0 0 24 24" aria-hidden="true">
      <text x="12" y="19" text-anchor="middle" font-family="Barlow, Arial, sans-serif" font-size="22" fill="var(--text-light)">@</text>
    </svg>
    <div class="contact contact--phone">555.038.6195</div>
    <div class="contact contact--email">delvin@tavrocapitalgroup.example</div>
  </section>

  <section class="card card--back" aria-label="Card back">
    <div class="bulb-art" role="img" aria-label="Sketched glowing light bulb illustration with radiating lines"></div>
    <svg class="bands" width="692" height="400" viewBox="0 0 692 400" aria-hidden="true">
      <polygon points="194,298 692,274 692,338 194,342" fill="var(--ink)"/>
      <polygon points="194,342 692,338 692,400 194,400" fill="var(--paper)"/>
      <rect x="0" y="310" width="194" height="54" fill="var(--paper)"/>
      <rect x="0" y="364" width="194" height="36" fill="var(--ink)"/>
    </svg>
    <div class="company">TAVRO Capital Group LLC</div>
  </section>

</main>
</body>
</html>
```